Safety Shoes Packaging - Box Design

We need a design for the box of safety shoes.
Our company is active in the industrial and construction sector.
Our brand logo is attached.
Also attached is the hang tag of the working gloves line for some consistency between the brand's product range.
They are intended for use in a wide variety of Industrial environments, like construction, cleaning and maintenance.
The final design should communicate
Safety
heavy duty use & toughness
durability
but also comfort and premium feel.
Packaging should also include a label with the following info - space:
Size:
Model:
Barcode
EN ISO 20345 S3 SRC
CE Symbol
Example of the label is also attached
Target Market(s)
Tradesmen, age 25-50
Industry/Entity Type
Construction, Landscape, Agriculture
Look and feel

```html
<!DOCTYPE html>
<html lang="en">
<head>
<meta charset="utf-8">
<title>KORVA Work + Safety Shoes – Box Design</title>
<link href="https://fonts.googleapis.com/css2?family=Montserrat:wght@400;500;800&display=swap" rel="stylesheet">
<style>
  :root {
    --bg: #d9d9d9;
    --box-black: #222223;
    --box-charcoal: #2e2e30;
    --texture-grey: #3a3a3c;
    --safety-orange: #e0643f;
    --white: #f2f2f2;
    --muted: #cfcfcf;
  }
  * { margin: 0; padding: 0; box-sizing: border-box; }
  html, body {
    width: 1200px; height: 1000px; overflow: hidden;
    background: var(--bg);
    font-family: "Montserrat", sans-serif;
  }
  .dieline {
    position: absolute; left: 100px; top: 70px;
    width: 1000px;
  }
  .panel {
    position: relative; overflow: hidden;
    background: var(--box-black);
    width: 1000px;
  }
  .panel--lid { height: 520px; }
  .panel--front { height: 300px; margin-top: 30px; }
  .hazard-bands { position: absolute; inset: 0; }
  .texture-zone {
    position: absolute; top: 0; right: 0; bottom: 0; width: 380px;
    background: linear-gradient(90deg, rgba(58,58,60,0) 0%, var(--texture-grey) 35%, var(--box-charcoal) 100%);
  }
  .brand-block {
    position: absolute; left: 0; right: 0; text-align: center;
    color: var(--white);
  }
  .brand-name {
    font-weight: 800; color: var(--safety-orange);
    letter-spacing: 10px; line-height: 1;
  }
  .brand-mark-square {
    display: inline-block; background: var(--safety-orange);
    vertical-align: middle;
  }
  .brand-tagline {
    font-weight: 800; letter-spacing: 2px; color: var(--white);
  }
  .product-title { font-weight: 800; color: var(--white); line-height: 1; }
  .product-title .light { font-weight: 400; }
  .origin-line { font-weight: 500; color: var(--muted); letter-spacing: 0.5px; }

  .panel--lid .brand-block { top: 130px; }
  .panel--lid .brand-name { font-size: 84px; }
  .panel--lid .brand-mark-square { width: 22px; height: 22px; margin-right: 18px; }
  .panel--lid .brand-tagline { font-size: 24px; margin-top: 10px; }
  .panel--lid .product-title { font-size: 46px; margin-top: 46px; }
  .panel--lid .origin-line { font-size: 16px; margin-top: 16px; }

  .panel--front .brand-block { top: 48px; }
  .panel--front .brand-name { font-size: 52px; }
  .panel--front .brand-mark-square { width: 14px; height: 14px; margin-right: 12px; }
  .panel--front .product-title { font-size: 44px; margin-top: 30px; }
  .panel--front .origin-line { font-size: 15px; margin-top: 14px; }
</style>
</head>
<body>
  <main class="dieline">
    <section class="panel panel--lid" aria-label="Box lid top">
      <svg class="hazard-bands" width="1000" height="520" viewBox="0 0 1000 520" aria-hidden="true">
        <polygon points="0,150 110,0 200,0 0,275" fill="var(--safety-orange)"/>
        <polygon points="330,0 440,0 330,150 250,150" fill="var(--safety-orange)"/>
        <polygon points="0,430 60,350 60,470 25,520 0,520" fill="var(--safety-orange)"/>
      </svg>
      <div class="texture-zone" role="img" aria-label="Perforated dot grid with fine crack lines texture"></div>
      <div class="brand-block">
        <div class="brand-name"><span class="brand-mark-square"></span>KORVA</div>
        <div class="brand-tagline">BUILT TO PROTECT</div>
        <div class="product-title">Work + Safety <span class="light">Shoes</span></div>
        <div class="origin-line">Designed by KORVA in Greece</div>
      </div>
    </section>

    <section class="panel panel--front" aria-label="Box front side">
      <svg class="hazard-bands" width="1000" height="300" viewBox="0 0 1000 300" aria-hidden="true">
        <polygon points="0,0 120,0 0,175" fill="var(--safety-orange)"/>
        <polygon points="0,250 40,190 40,300 0,300" fill="var(--safety-orange)"/>
      </svg>
      <div class="texture-zone" role="img" aria-label="Perforated dot grid with fine crack lines texture"></div>
      <div class="brand-block">
        <div class="brand-name"><span class="brand-mark-square"></span>KORVA</div>
        <div class="product-title">Work + Safety <span class="light">Shoes</span></div>
        <div class="origin-line">Designed by KORVA in Greece</div>
      </div>
    </section>
  </main>
</body>
</html>
```